Software engineering company needs business card

I need a cool business card. Company: Byte Merano Larchwood Ave 41 58213 Dunmere Name: Gerald Hofmann CEO / Managing Director & Owner

Industry/Entity Type

Business

```html
<!DOCTYPE html>
<html lang="en">
<head>
<meta charset="utf-8">
<title>Byte Merano – Business Card</title>
<link rel="stylesheet" href="https://fonts.googleapis.com/css2?family=Encode+Sans+Condensed:wght@400;500&display=swap">
<style>
  :root {
    --page-bg: #eef0f0;
    --card-dark: #22292a;
    --band-green: #2cb514;
    --fold-green: #229a10;
    --band-white: #ffffff;
    --fold-grey: #a9b8bb;
    --accent-square: #8cd61c;
    --wordmark: #4a5356;
    --text-light: #ffffff;
  }
  * { margin: 0; padding: 0; box-sizing: border-box; }
  html, body {
    width: 1200px;
    height: 991px;
    overflow: hidden;
    background: var(--page-bg);
    font-family: "Encode Sans Condensed", "Arial Narrow", sans-serif;
  }
  .card {
    position: absolute;
    left: 250px;
    width: 700px;
    height: 437px;
    background: var(--card-dark);
    overflow: hidden;
    box-shadow: 0 6px 18px rgba(0,0,0,0.25);
  }
  .card--contact { top: 38px; }
  .card--brand { top: 515px; }
  .card svg.card-art {
    position: absolute;
    inset: 0;
    width: 700px;
    height: 437px;
  }
  .band-shadow { fill: rgba(0,0,0,0.35); }
  .band { fill: var(--band-green); }
  .fold { fill: var(--fold-green); }
  .band-white { fill: var(--band-white); }
  .fold-grey { fill: var(--fold-grey); }
  .icon { fill: var(--text-light); }
  .icon-stroke { fill: none; stroke: var(--text-light); }

  .contact-text {
    position: absolute;
    color: var(--text-light);
    line-height: 1.15;
    white-space: nowrap;
  }
  .contact-name {
    left: 30px; top: 66px;
    font-size: 26px;
    text-transform: uppercase;
  }
  .contact-role {
    left: 30px; top: 100px;
    font-size: 17px;
  }
  .contact-phone {
    left: 405px; top: 106px;
    font-size: 22px;
  }
  .contact-address {
    left: 30px; top: 270px;
    font-size: 20px;
  }
  .contact-email {
    left: 410px; top: 302px;
    font-size: 21px;
  }
  .at-sign {
    position: absolute;
    left: 640px; top: 270px;
    width: 50px;
    text-align: center;
    color: var(--text-light);
    font-size: 44px;
    font-weight: 500;
  }

  .brand-square {
    position: absolute;
    left: 192px; top: 187px;
    width: 36px; height: 36px;
    background: var(--accent-square);
  }
  .brand-name {
    position: absolute;
    left: 340px; top: 204px;
    font-size: 36px;
    font-weight: 500;
    letter-spacing: 7px;
    color: var(--wordmark);
    text-transform: uppercase;
    white-space: nowrap;
  }
</style>
</head>
<body>

<section class="card card--contact">
  <svg class="card-art" viewBox="0 0 700 437" aria-hidden="true">
    <!-- upper band -->
    <polygon class="band-shadow" points="0,140 240,140 275,125 345,125 385,165 600,165 625,150 700,150 700,175 625,175 600,190 385,190 345,150 275,150 240,165 0,165"/>
    <polygon class="band" points="0,55 240,55 240,140 0,140"/>
    <polygon class="fold" points="240,55 275,35 275,125 240,140"/>
    <polygon class="band" points="275,35 345,35 345,125 275,125"/>
    <polygon class="fold" points="345,35 385,75 385,165 345,125"/>
    <polygon class="band" points="385,75 600,75 600,165 385,165"/>
    <polygon class="fold" points="600,75 625,60 625,150 600,165"/>
    <polygon class="band" points="625,60 700,60 700,150 625,150"/>

    <!-- lower band -->
    <polygon class="band-shadow" points="0,340 250,340 285,320 355,320 395,360 590,360 620,340 700,340 700,365 620,365 590,385 395,385 355,345 285,345 250,365 0,365"/>
    <polygon class="band" points="0,255 250,255 250,340 0,340"/>
    <polygon class="fold" points="250,255 285,235 285,320 250,340"/>
    <polygon class="band" points="285,235 355,235 355,320 285,320"/>
    <polygon class="fold" points="355,235 395,275 395,360 355,320"/>
    <polygon class="band" points="395,275 590,275 590,360 395,360"/>
    <polygon class="fold" points="590,275 620,255 620,340 590,360"/>
    <polygon class="band" points="620,255 700,255 700,340 620,340"/>

    <!-- person icon -->
    <g class="person-icon">
      <circle class="icon" cx="310" cy="70" r="13"/>
      <path class="icon" d="M287,104 Q289,86 310,86 Q331,86 333,104 Z"/>
      <path class="icon-stroke" stroke-width="3" d="M295,72 Q295,52 310,52 Q325,52 325,72"/>
      <path class="icon-stroke" stroke-width="2" d="M325,74 Q324,84 314,84"/>
    </g>

    <!-- phone icon -->
    <path class="icon" d="M648,88 q4,-6 10,-2 l6,7 q2,4 -2,7 l-4,3 q3,10 14,18 l3,-4 q3,-3 7,-1 l7,6 q3,5 -2,9 l-4,4 q-8,5 -22,-6 q-14,-12 -16,-28 q0,-7 3,-13 z"/>

    <!-- home icon -->
    <g class="home-icon">
      <polygon class="icon" points="320,252 296,274 301,279 320,262 339,279 344,274"/>
      <polygon class="icon" points="304,280 320,266 336,280 336,300 325,300 325,288 315,288 315,300 304,300"/>
    </g>
  </svg>

  <div class="contact-text contact-name">Gerald Hofmann</div>
  <div class="contact-text contact-role">CEO / Managing Director &amp; Owner</div>
  <div class="contact-text contact-phone">+49 7031 480592</div>
  <div class="contact-text contact-address">Larchwood Ave 41<br>58213 Dunmere</div>
  <div class="contact-text contact-email">info (at) bytemerano.de</div>
  <div class="at-sign">@</div>
</section>

<section class="card card--brand">
  <svg class="card-art" viewBox="0 0 700 437" aria-hidden="true">
    <polygon class="band-shadow" points="0,290 110,290 150,270 270,270 310,290 700,290 700,312 310,312 270,292 150,292 110,312 0,312"/>
    <polygon class="band-white" points="0,165 110,165 110,290 0,290"/>
    <polygon class="fold-grey" points="110,165 150,140 150,270 110,290"/>
    <polygon class="band-white" points="150,140 270,140 270,270 150,270"/>
    <polygon class="fold-grey" points="270,140 310,165 310,290 270,270"/>
    <polygon class="band-white" points="310,165 700,165 700,290 310,290"/>
  </svg>
  <div class="brand-square"></div>
  <div class="brand-name">Byte Merano</div>
</section>

</body>
</html>
```